Business Card Design Project (Beer industry)

I am seeking a redesign of my business card. I am looking for something that will really stand out in both texture and feel. Something more on the modern side then traditional. Nothing die cut shaped like a beer mug please.

The card is used mostly for other industry professionals, as well as bar and restaurant owners. My title is Strategy & Acquisitions. If you would like to somehow incorporate that theme, that may work.

My business is craft and imported beer. Nothing fizzy and yellow, so my products are more on the upscale side.
Updates

I was able to update my logo in .ai and .tif format. I hope that helps. 

Thank you all for your creative ideas. I have uploaded my current business card in pdf format, as well as our logo in .eps file format. We are excited about the submissions so far and want to thank you all again.

PS Please do not include fax number in future submissions, as we are looking for something more creative and a fax says 1999 and not 2015, which is the message we are going for, without being futuristic. 

Thank you all once again for all of your submissions. If we would consider a two sided card, we would like the opposite side not to be the same as the front. The styles we have seen so far, it appears the front and back are too similar. Again, a two sided card is not required. Thank you and we look forward to pushing the boundaries of your creativity. Cheers

Target Market(s)

My card would mostly go to bar and restaurant operators as well as other beer industry professionals

Industry/Entity Type

Restaurant

Requirements
Nice to have
• Two sided would be considered, although not required
Should not have
• Anything die cut shaped like a beer mug.

```html
<!DOCTYPE html>
<html lang="en">
<head>
<meta charset="utf-8">
<title>Kestrel Beer – Business Card</title>
<link href="https://fonts.googleapis.com/css2?family=Montserrat:wght@400;600&family=Cormorant+Garamond:ital,wght@1,600&display=swap" rel="stylesheet">
<style>
  :root {
    --page-bg: #33261e;
    --band-light: #6a6a6a;
    --band-mid: #4a4a4a;
    --panel-dark: #2c2c2c;
    --panel-deep: #232323;
    --text-light: #d9d9d9;
    --text-soft: #b5b5b5;
    --tagline-ink: #161616;
    --rule: #8a8a8a;
    --glint: rgba(255,255,255,0.85);
  }
  html, body {
    margin: 0;
    width: 1200px;
    height: 900px;
    overflow: hidden;
    background: var(--page-bg);
  }
  .card {
    position: absolute;
    left: 100px;
    top: 190px;
    width: 1000px;
    height: 520px;
    border-radius: 26px;
    overflow: hidden;
    background: linear-gradient(180deg, var(--band-light) 0%, var(--band-mid) 100%);
    box-shadow: 0 18px 40px rgba(0,0,0,0.55);
    font-family: "Montserrat", sans-serif;
    color: var(--text-light);
  }
  .card__top-band {
    position: absolute; left: 0; top: 0; width: 100%; height: 86px;
    background: linear-gradient(180deg, #7a7a7a 0%, #5a5a5a 100%);
  }
  .card__panel {
    position: absolute; left: 0; top: 86px; width: 100%; height: 344px;
    background: radial-gradient(ellipse at 50% 40%, var(--panel-dark) 0%, var(--panel-deep) 100%);
    border-top: 2px solid #9a9a9a;
    border-bottom: 2px solid #9a9a9a;
    box-shadow: inset 0 8px 14px rgba(0,0,0,0.5), inset 0 -8px 14px rgba(0,0,0,0.5);
  }
  .card__bottom-band {
    position: absolute; left: 0; top: 432px; width: 100%; height: 88px;
    background: linear-gradient(180deg, #6e6e6e 0%, #525252 100%);
  }
  .glint {
    position: absolute; width: 70px; height: 14px; border-radius: 50%;
    background: radial-gradient(ellipse, var(--glint) 0%, rgba(255,255,255,0) 70%);
  }
  .brand {
    position: absolute; left: 52px; top: 150px;
    display: flex; align-items: center; gap: 12px;
    font-weight: 600; font-size: 30px; color: var(--text-light);
  }
  .brand__dot {
    width: 22px; height: 22px; border-radius: 50%; background: var(--text-light);
  }
  .person {
    position: absolute; left: 370px; top: 150px; width: 240px; text-align: center;
  }
  .person__name { font-weight: 600; font-size: 26px; color: var(--text-light); }
  .person__title { font-size: 13px; color: var(--text-soft); margin-top: 2px; }
  .divider {
    position: absolute; width: 2px; background: var(--rule);
  }
  .contact {
    position: absolute; display: flex; flex-direction: column; gap: 22px;
    font-size: 20px; color: var(--text-soft);
  }
  .contact__item { display: flex; align-items: center; gap: 18px; }
  .contact__icon { width: 22px; height: 22px; flex: none; }
  .address {
    position: absolute; left: 300px; top: 378px; width: 500px; text-align: center;
    font-size: 20px; color: var(--text-soft);
  }
  .tagline {
    position: absolute; left: 0; top: 452px; width: 100%; text-align: center;
    font-family: "Cormorant Garamond", serif; font-style: italic; font-weight: 600;
    font-size: 36px; color: var(--tagline-ink); letter-spacing: 0.5px;
  }
</style>
</head>
<body>
<div class="card">
  <div class="card__top-band"></div>
  <div class="card__panel"></div>
  <div class="card__bottom-band"></div>

  <span class="glint" style="left:90px;top:80px"></span>
  <span class="glint" style="left:300px;top:80px"></span>
  <span class="glint" style="left:520px;top:80px"></span>
  <span class="glint" style="left:740px;top:80px"></span>
  <span class="glint" style="left:900px;top:80px"></span>
  <span class="glint" style="left:120px;top:425px"></span>
  <span class="glint" style="left:360px;top:425px"></span>
  <span class="glint" style="left:600px;top:425px"></span>
  <span class="glint" style="left:850px;top:425px"></span>

  <div class="brand"><span class="brand__dot"></span>Kestrel Beer</div>

  <div class="person">
    <div class="person__name">Dan Verlo</div>
    <div class="person__title">sales manager</div>
  </div>

  <div class="divider" style="left:640px;top:190px;height:90px"></div>
  <div class="contact" style="left:670px;top:192px">
    <div class="contact__item">
      <svg class="contact__icon" viewBox="0 0 24 24"><circle cx="12" cy="12" r="4" fill="none" stroke="#d9d9d9" stroke-width="2.4"/><path d="M16 8v6a2.5 2.5 0 0 0 5 0v-2a9 9 0 1 0-4 7.5" fill="none" stroke="#d9d9d9" stroke-width="2.4"/></svg>
      <span>dverlo@mail.com</span>
    </div>
    <div class="contact__item">
      <svg class="contact__icon" viewBox="0 0 24 24"><path d="M2 12 12 3l10 9h-3v9h-5v-6h-4v6H5v-9z" fill="#d9d9d9"/></svg>
      <span>www.kestrelbeer.com</span>
    </div>
  </div>

  <div class="divider" style="left:232px;top:290px;height:100px"></div>
  <div class="contact" style="left:262px;top:292px">
    <div class="contact__item">
      <svg class="contact__icon" viewBox="0 0 24 24"><rect x="6" y="2" width="12" height="20" rx="2" fill="none" stroke="#d9d9d9" stroke-width="2"/><line x1="10" y1="18" x2="14" y2="18" stroke="#d9d9d9" stroke-width="2"/></svg>
      <span>(555) 014-2291</span>
    </div>
    <div class="contact__item">
      <svg class="contact__icon" viewBox="0 0 24 24"><circle cx="12" cy="12" r="10" fill="none" stroke="#d9d9d9" stroke-width="2"/><path d="M9 7c-1 1-1 3 1 6s4 4 5 4l1.5-1.5-2-2-1 1c-1-.5-2-1.5-2.5-2.5l1-1-2-2z" fill="#d9d9d9"/></svg>
      <span>(555) 018-6630</span>
    </div>
  </div>

  <div class="address">42 Foundry Street Riverton, NY 10000</div>

  <div class="tagline">Premier Craft &amp; Import Beer Distributor</div>
</div>
</body>
</html>
```